Food Safety 1-California workers only

3.25" by 4.5" Black and White Magazine Ad
This ad is to train California workers only.
Workers will be trained on: Food Safety, FSMA (Food Safety Modernization Act), using equipment safety, food processing production skills, worker safety, supervisory skills, communication skills.
"FREE TRAINING", The company does the training or Harbor Learning will provide the training.
Training grants range from $100,000 to $400,000.
Companies must be in business for profit.
Companies must train 200 employees or more.
This program is for California workers only.
Incumbent or new-hires are eligible.

Target Market(s)

California food processors, farms, food packaging, food processors, companies under FSMA, food safety, food production who need to train employees.

Industry/Entity Type

Food Production

Font styles to use
Serif
Sans Serif

Colors

Designer to choose colors to be used in the design.

Requirements
Must have
• This is a 3.25 inch by 4.5 inch magazine ad. It must be black and white. No color.
• The deliverable must be in basic PhotoShop. The ad does not need to include any graphics and be text only if needed. If you have a black and white graphic that will show well.
• Look at www.BQXFoodSafety..com
• Use the text from "FOOD2U-Photoshop-052018" file as your starting point.
Nice to have
• A black and white graphic about food. See www.BQXFoodSafety.com
Should not have
• No color.

```html
<!DOCTYPE html>
<html lang="en">
<head>
<meta charset="utf-8">
<title>Free Training – Harbor Learning</title>
<link rel="stylesheet" href="https://fonts.googleapis.com/css2?family=Anton&family=Oswald:wght@600;700&family=Lato:wght@700;900&family=Tinos:wght@700&display=swap">
<style>
  :root {
    --ink: #000000;
    --paper: #ffffff;
    --backdrop: #3d3d3f;
  }
  * { margin: 0; padding: 0; box-sizing: border-box; }
  html, body {
    width: 914px; height: 1200px; overflow: hidden;
    background: var(--backdrop);
  }
  .ad {
    position: absolute; left: 118px; top: 132px;
    width: 678px; height: 936px;
    background: var(--paper); color: var(--ink);
    overflow: hidden;
  }
  .headline {
    position: absolute; left: 0; width: 100%; top: 44px;
    text-align: center;
    font-family: "Anton", "Oswald", sans-serif; font-weight: 400;
    font-size: 90px; line-height: 1; letter-spacing: 1px;
    transform: scaleX(1.28); transform-origin: center top;
  }
  .topic-band {
    position: absolute; left: 14px; top: 155px; width: 654px; height: 57px;
  }
  .topic-band svg { position: absolute; inset: 0; }
  .topic-band p {
    position: relative; text-align: center;
    font-family: "Oswald", sans-serif; font-weight: 700;
    font-size: 24px; line-height: 57px; color: var(--paper);
    letter-spacing: 0.2px;
  }
  .slogan {
    position: absolute; left: 0; width: 100%; top: 225px;
    text-align: center;
    font-family: "Anton", "Oswald", sans-serif; font-weight: 400;
    font-size: 46px; line-height: 69px;
    transform: scaleX(1.27); transform-origin: center top;
  }
  .rule {
    position: absolute; left: 0; width: 100%; top: 384px; height: 10px;
    background: var(--ink);
  }
  .qualify {
    position: absolute; left: 0; width: 100%; top: 403px; height: 297px;
    background: var(--ink); color: var(--paper);
    font-family: "Tinos", "Times New Roman", serif; font-weight: 700;
    padding: 20px 0 0 50px;
  }
  .qualify h2 { font-size: 32px; line-height: 1; margin-bottom: 14px; font-weight: 700; }
  .qualify ul { list-style: none; font-size: 22px; line-height: 27.8px; }
  .qualify li::before { content: "• "; }
  .contact-tab {
    position: absolute; left: 240px; top: 711px; width: 198px; height: 43px;
  }
  .contact-tab svg { position: absolute; inset: 0; }
  .contact-tab p {
    position: relative; text-align: center;
    font-family: "Lato", sans-serif; font-weight: 900;
    font-size: 28px; line-height: 43px; color: var(--paper);
  }
  .contact-col {
    position: absolute; top: 782px;
    font-family: "Lato", sans-serif; font-weight: 700; font-style: normal;
    font-size: 22.5px; line-height: 28px;
  }
  .contact-col.person { left: 22px; }
  .contact-col.channels { left: 383px; }
</style>
</head>
<body>
  <main class="ad">
    <h1 class="headline">FREE TRAINING</h1>

    <div class="topic-band">
      <svg width="654" height="57" viewBox="0 0 654 57" aria-hidden="true">
        <polygon points="0,0 654,0 646,57 8,57" fill="var(--ink)"/>
      </svg>
      <p>FOOD SAFETY (FSMA) PRODUCTION SKILLS WORKER SAFETY</p>
    </div>

    <p class="slogan">“WE DO THE TRAINING AND<br>THE STATE PAYS FOR IT!”</p>

    <div class="rule"></div>

    <section class="qualify">
      <h2>How to Qualify:</h2>
      <ul>
        <li>Train California Workers Only</li>
        <li>Trainees must earn $11/hour</li>
        <li>Full-time workers only</li>
        <li>Employees must attend at least 8 Hours of training</li>
        <li>You must train 200 or more employees</li>
        <li>Incumbent or New-Hire workers are eligible</li>
        <li>Seasonal workers are eligibl</li>
      </ul>
    </section>

    <div class="contact-tab">
      <svg width="198" height="43" viewBox="0 0 198 43" aria-hidden="true">
        <polygon points="0,0 198,0 184,43 14,43" fill="var(--ink)"/>
      </svg>
      <p>CONTACT:</p>
    </div>

    <address class="contact-col person">
      Daniel Morrow<br>
      Harbor Learning Company, Inc.<br>
      2150 Lakeview Avenue,<br>
      Suite 310, Irvine, CA 92618
    </address>
    <address class="contact-col channels">
      www.HLCCAL.com<br>
      www.BQXFoodSafety.com<br>
      Dan.Morrow@HLCCAL.com<br>
      Phone: (949) 555-0148
    </address>
  </main>
</body>
</html>
```